A5 spiral bound, full colour, baby massage booklet

We need full design of an A5 instruction booklet on baby massage to help parents remember what they have learned at baby massage classes. The booklet will be bi-lingual with text in english and mandarin. Designs need to be in line with the look of the Cradle Touch Guidance Network website (cradletouchhub.net.au) and other Cradle Touch Guidance products.
To give an indication of length, our current manual (which is in need of refreshing and updating being monotone and in English only is 30 pages.)
We need a print ready file or folder that can be provided to a printer to produce the final product.

Target Market(s)

Parents wanting to learn baby massage

Industry/Entity Type

Baby massage

Colors
6B429C
8869AF
B7A5CE
E3DAEB
F3F0F8

Requirements
Nice to have
• Logo, images of massage techniques coupled with English and Mandarin instructions

```html
<!DOCTYPE html>
<html lang="en">
<head>
<meta charset="utf-8">
<title>Baby Massage Booklet Cover</title>
<link href="https://fonts.googleapis.com/css2?family=Poppins:wght@400;500;600&family=Noto+Sans+TC:wght@400;500&display=swap" rel="stylesheet">
<style>
  :root {
    --purple-deep: #5E3596;
    --purple: #6B429C;
    --purple-mid: #8869AF;
    --purple-soft: #B7A5CE;
    --lilac: #E3DAEB;
    --lilac-pale: #F3F0F8;
    --white: #FFFFFF;
    --stage: #B3DCEC;
  }
  * { margin: 0; padding: 0; box-sizing: border-box; }
  html, body { width: 1200px; height: 780px; overflow: hidden; }
  body {
    background: var(--stage);
    display: flex; align-items: center; justify-content: center;
    font-family: "Poppins", "Noto Sans TC", sans-serif;
  }
  .cover {
    position: relative;
    width: 510px; height: 720px;
    background: var(--purple);
    overflow: hidden;
    box-shadow: 0 6px 18px rgba(60, 40, 100, 0.25);
  }
  .cover-facets { position: absolute; inset: 0; }
  .title-block {
    position: absolute; top: 78px; left: 0; right: 0;
    text-align: center; color: var(--white);
  }
  .title-en {
    font-weight: 600; font-size: 40px; letter-spacing: 4px; line-height: 1.1;
  }
  .title-zh {
    font-family: "Noto Sans TC", sans-serif;
    font-weight: 500; font-size: 40px; letter-spacing: 4px; line-height: 1.25;
  }
  .title-rule {
    position: absolute; top: 182px; left: 30px; right: 0;
    height: 2px; background: var(--white);
  }
  .photo {
    position: absolute; top: 200px; left: 0; right: 0; height: 250px;
    background: linear-gradient(100deg, var(--lilac) 0%, #E9D8B8 22%, var(--purple-deep) 45%, #EBC9AE 70%, var(--purple-mid) 100%);
  }
  .photo-rule {
    position: absolute; top: 450px; left: 0; right: 0; height: 12px;
    background: var(--purple-deep);
  }
  .info-band {
    position: absolute; top: 462px; left: 0; right: 0; height: 116px;
    background: var(--lilac-pale);
    color: var(--purple);
    text-align: center;
    padding-top: 14px;
  }
  .info-line { font-size: 16px; font-weight: 400; line-height: 1.3; }
  .info-line-zh {
    font-family: "Noto Sans TC", sans-serif;
    font-size: 15px; line-height: 1.35; margin-bottom: 4px;
  }
  .base-band {
    position: absolute; top: 578px; left: 0; right: 0; bottom: 0;
    background: var(--purple-deep);
  }
  .language-label {
    position: absolute; right: 36px; top: 610px;
    color: var(--white); text-align: center;
    font-size: 15px; line-height: 1.4;
  }
  .language-label .zh { font-family: "Noto Sans TC", sans-serif; }
</style>
</head>
<body>
  <main class="cover">
    <svg class="cover-facets" width="510" height="720" viewBox="0 0 510 720" aria-hidden="true">
      <rect width="510" height="720" fill="var(--purple-mid)"/>
      <polygon points="0,0 510,0 510,40 0,60" fill="var(--purple-deep)"/>
      <polygon points="330,200 510,160 510,450 420,450" fill="var(--purple-soft)"/>
      <polygon points="0,200 120,200 0,320" fill="var(--lilac)"/>
    </svg>

    <header class="title-block">
      <h1 class="title-en">BABY MASSAGE</h1>
      <p class="title-zh" lang="zh-Hant">嬰兒按摩</p>
    </header>
    <div class="title-rule"></div>

    <div class="photo" role="img" aria-label="Photo of a smiling baby lying on a white blanket while a parent's hands massage its back"></div>
    <div class="photo-rule"></div>

    <section class="info-band">
      <p class="info-line">Your step-by-step Guide for Massage time</p>
      <p class="info-line-zh" lang="zh-Hant">給家長的嬰兒按摩指南</p>
      <p class="info-line">Produce by the Cradle Touch Guidance Network</p>
      <p class="info-line-zh" lang="zh-Hant">搖籃撫觸指導網絡出版</p>
    </section>

    <div class="base-band"></div>
    <p class="language-label">Traditional Chinese/English<br><span class="zh" lang="zh-Hant">（繁體中文/英文）</span></p>
  </main>
</body>
</html>
```